Finiding oppertunites in Real Estate 6.15.20

size of ad 7” x 9.6”
1-I like the ad to stand out and attract people's attention.
2-you should be able to see the text of the ad clearly .. see the attachment anything in yellow is instructions.
3-the list of topics should not be the main part of the ad
4-if you decide you want a picture or vector of a person .. (you decide)
then it should be a white male about 25-30 years old wearing a solid white or blue shirt and not long hair.
5-leave 1 inch for footer
see attachment
Good luck

Target Market(s)

potential male students 25-35 years of age

Industry/Entity Type

Education

Requirements
Must have
• will stand out and people would want to see it.
should be able to read the words of ad
Nice to have
• how to make money in real estate on one line

```html
<!DOCTYPE html>
<html lang="en">
<head>
<meta charset="utf-8">
<title>Real Estate Career Course Flyer</title>
<link href="https://fonts.googleapis.com/css2?family=Bebas+Neue&family=Montserrat:wght@500;800&display=swap" rel="stylesheet">
<style>
  :root {
    --stage: #cbcbcb;
    --brand-blue: #1a8fd9;
    --blue-deep: #1479c0;
    --ink: #0b0b0b;
    --paper: #ffffff;
  }
  html, body {
    margin: 0;
    padding: 0;
    width: 1200px;
    height: 615px;
    overflow: hidden;
    background: var(--stage);
  }
  .flyer {
    position: absolute;
    left: 389px;
    top: 17px;
    width: 801px;
    height: 1100px;
    transform: scale(0.5273);
    transform-origin: top left;
    background: var(--paper);
    overflow: hidden;
    font-family: "Montserrat", Arial, sans-serif;
    box-shadow: 0 6px 24px rgba(0,0,0,0.18);
  }
  .flyer-body {
    position: absolute;
    left: 0; top: 0;
    width: 801px;
    height: 1035px;
    background: var(--brand-blue);
    overflow: hidden;
  }
  .footer-space {
    position: absolute;
    left: 0; top: 1035px;
    width: 801px; height: 65px;
    background: var(--paper);
  }
  .house-backdrop {
    position: absolute;
    left: 250px; top: 410px;
    width: 450px; height: 330px;
    background: linear-gradient(180deg, rgba(20,80,140,0.18), rgba(20,80,140,0.05));
  }
  .presenter-photo {
    position: absolute;
    left: 470px; top: 440px;
    width: 331px; height: 595px;
    background: linear-gradient(180deg, rgba(240,244,248,0.55) 0%, rgba(235,240,246,0.75) 40%, rgba(255,255,255,0.8) 100%);
    border-radius: 140px 140px 0 0;
  }
  .title-disc {
    position: absolute;
    left: 0; top: 0;
  }
  .title {
    position: absolute;
    left: 45px; top: 36px;
    margin: 0;
    font-family: "Bebas Neue", Impact, sans-serif;
    font-weight: 400;
    line-height: 0.86;
  }
  .title-kicker { display: block; font-size: 58px; color: var(--ink); }
  .title-main { display: block; font-size: 100px; color: var(--blue-deep); margin-top: 8px; }
  .intro-points {
    position: absolute;
    left: 398px; top: 44px;
    width: 370px;
    margin: 0; padding: 0;
    list-style: none;
    color: var(--paper);
    font-size: 15.5px;
    font-weight: 500;
    line-height: 21px;
  }
  .intro-points li {
    position: relative;
    padding-left: 19px;
    margin-bottom: 11px;
  }
  .intro-points li::before {
    content: "";
    position: absolute;
    left: 0; top: 7px;
    width: 7px; height: 7px;
    border-radius: 50%;
    background: var(--ink);
    box-shadow: 0 0 0 1.5px var(--paper);
  }
  .sessions-heading {
    position: absolute;
    left: 397px; top: 196px;
    margin: 0;
    font-family: "Bebas Neue", Impact, sans-serif;
    font-weight: 400;
    font-size: 72px;
    line-height: 1;
    color: var(--ink);
    -webkit-text-stroke: 2px var(--paper);
    paint-order: stroke fill;
    letter-spacing: -0.5px;
  }
  .sessions-rule {
    position: absolute;
    left: 398px; top: 273px;
    width: 357px; height: 3px;
    background: var(--paper);
  }
  .schedule {
    position: absolute;
    left: 398px; top: 287px;
    margin: 0;
    font-weight: 800;
    font-size: 29px;
    line-height: 38px;
    color: var(--paper);
  }
  .schedule .date { color: var(--ink); }
  .topics-heading {
    position: absolute;
    left: 45px; top: 360px;
    margin: 0;
    font-family: "Bebas Neue", Impact, sans-serif;
    font-weight: 400;
    font-size: 52px;
    line-height: 0.95;
    color: var(--paper);
  }
  .topics-heading .dark { color: var(--ink); display: block; }
  .topics {
    position: absolute;
    left: 48px; top: 472px;
    margin: 0; padding: 0;
    list-style: none;
    color: var(--paper);
    font-size: 20px;
    font-weight: 500;
  }
  .topics li {
    display: flex;
    align-items: center;
    height: 42.5px;
  }
  .topic-icon {
    width: 33px; height: 33px;
    margin-right: 9px;
    flex: none;
  }
</style>
</head>
<body>
<div class="flyer">
  <div class="flyer-body">
    <div class="house-backdrop" role="img" aria-label="Faded photo of a modern house"></div>

    <svg class="title-disc" width="801" height="460" viewBox="0 0 801 460" aria-hidden="true">
      <ellipse cx="118" cy="66" rx="242" ry="280" fill="#0b0b0b"/>
      <ellipse cx="120" cy="56" rx="240" ry="276" fill="#ffffff"/>
    </svg>

    <h1 class="title">
      <span class="title-kicker">Real Estate</span>
      <span class="title-main">Career<br>Course</span>
    </h1>

    <ul class="intro-points">
      <li>How to Make Money In Real Estate?</li>
      <li>An investment in knowledge opens up untold opportunities</li>
      <li>For those who have started or would like to go into Real Estate</li>
    </ul>

    <h2 class="sessions-heading">Remote Sessions</h2>
    <div class="sessions-rule"></div>
    <p class="schedule">12 SESSION COURSE<br>CLASSES STARTING<br><span class="date">JUNE 16</span></p>

    <h2 class="topics-heading">A Partial Listing<span class="dark">of Topics</span></h2>

    <div class="presenter-photo" role="img" aria-label="Photo of a young man in a white shirt pointing toward the topic list"></div>

    <ul class="topics">
      <li><svg class="topic-icon" viewBox="0 0 34 34"><circle cx="17" cy="17" r="16" fill="#fff"/><circle cx="17" cy="12" r="4" fill="#0b0b0b"/><rect x="12" y="17" width="10" height="9" rx="3" fill="#0b0b0b"/></svg>Single-family</li>
      <li><svg class="topic-icon" viewBox="0 0 34 34"><circle cx="17" cy="17" r="16" fill="#fff"/><path d="M8 17 L17 9 L26 17 V25 H8 Z" fill="#0b0b0b"/></svg>Multifamily</li>
      <li><svg class="topic-icon" viewBox="0 0 34 34"><circle cx="17" cy="17" r="16" fill="#fff"/><circle cx="17" cy="12" r="4" fill="#0b0b0b"/><path d="M10 26 Q17 14 24 26 Z" fill="#0b0b0b"/></svg>Management</li>
      <li><svg class="topic-icon" viewBox="0 0 34 34"><circle cx="17" cy="17" r="16" fill="#fff"/><path d="M8 16 L17 9 L26 16 H23 V25 H11 V16 Z" fill="#0b0b0b"/></svg>Real Estate Concepts</li>
      <li><svg class="topic-icon" viewBox="0 0 34 34"><circle cx="17" cy="17" r="16" fill="#fff"/><path d="M9 17 L17 10 L25 17 M12 15 V25 H22 V15" fill="none" stroke="#0b0b0b" stroke-width="2"/></svg>Real Estate law</li>
      <li><svg class="topic-icon" viewBox="0 0 34 34"><circle cx="17" cy="17" r="16" fill="#fff"/><circle cx="17" cy="17" r="8" fill="none" stroke="#0b0b0b" stroke-width="2"/><text x="17" y="21.5" font-size="12" text-anchor="middle" font-family="Arial, sans-serif" font-weight="700">$</text></svg>Investment properties</li>
      <li><svg class="topic-icon" viewBox="0 0 34 34"><circle cx="17" cy="17" r="16" fill="#fff"/><path d="M8 19 L17 11 L26 19 V25 H8 Z" fill="#0b0b0b"/></svg>Foreclosures</li>
      <li><svg class="topic-icon" viewBox="0 0 34 34"><circle cx="17" cy="17" r="16" fill="#fff"/><rect x="10" y="10" width="9" height="5" fill="#0b0b0b"/><rect x="13" y="15" width="3" height="11" fill="#0b0b0b"/></svg>Rehab</li>
      <li><svg class="topic-icon" viewBox="0 0 34 34"><circle cx="17" cy="17" r="16" fill="#fff"/><rect x="10" y="19" width="3" height="6" fill="#0b0b0b"/><rect x="15" y="15" width="3" height="10" fill="#0b0b0b"/><rect x="20" y="11" width="3" height="14" fill="#0b0b0b"/></svg>Short sales</li>
      <li><svg class="topic-icon" viewBox="0 0 34 34"><circle cx="17" cy="17" r="16" fill="#fff"/><circle cx="17" cy="13" r="4" fill="none" stroke="#0b0b0b" stroke-width="2"/><path d="M10 25 Q17 18 24 25" fill="none" stroke="#0b0b0b" stroke-width="2"/></svg>Development</li>
      <li><svg class="topic-icon" viewBox="0 0 34 34"><circle cx="17" cy="17" r="16" fill="#fff"/><rect x="11" y="9" width="12" height="16" fill="none" stroke="#0b0b0b" stroke-width="2"/><path d="M14 14 H20 M14 18 H20" stroke="#0b0b0b" stroke-width="2"/></svg>Finical modeling</li>
      <li><svg class="topic-icon" viewBox="0 0 34 34"><circle cx="17" cy="17" r="16" fill="#fff"/><path d="M7 16 L17 10 L27 16 Z M11 17 H23 V24 H11 Z" fill="#0b0b0b"/></svg>HUD properties</li>
      <li><svg class="topic-icon" viewBox="0 0 34 34"><circle cx="17" cy="17" r="16" fill="#fff"/><circle cx="15" cy="15" r="6" fill="none" stroke="#0b0b0b" stroke-width="2.5"/><path d="M19 19 L25 25" stroke="#0b0b0b" stroke-width="3"/></svg>Due Diligence</li>
    </ul>
  </div>
  <div class="footer-space"></div>
</div>
</body>
</html>
```